Business Card Design Project for an English Teacher

I need a business card design for my new job.
I'd like to start teaching English as a freelance.
My students will be children, teenager, and adults, who don't like or hesitate to study English and I would like to open a door to the new world for them.

I'd like to put the information below;
[right side]
1. name
2. mail address
3. mobile number
4. website or facebook page

[back]
1.my message: Feel free at asking me anything about my classes

2.lesson list such as:
price: 3150 yen ~

calsses:
kids class( mum& dad can join) ... 30 minutes / 45 minutes
students (over age 13).... 60minutes / 90 minutes
Adult (over age 19) .... 60 minutes / 90 minutes

3. I'll have both Web Lesson and Face to Face Lesson

4. Free trial lesson

Target Market(s)

My students will be children, teenager, and adults, who don't like or hesitate to study English

Industry/Entity Type

Business

Requirements
Must have
• designed both side

```html
<!DOCTYPE html>
<html lang="en">
<head>
<meta charset="utf-8">
<title>Mika Arai – English Instructor Business Card</title>
<link rel="stylesheet" href="https://fonts.googleapis.com/css2?family=Cardo:wght@400;700&family=Lato:wght@400;700&display=swap">
<style>
  :root {
    --stage: #5e4637;
    --kraft-light: #e2d6c0;
    --kraft-mid: #d6c8ae;
    --kraft-pale: #ebe2d1;
    --kraft-dark: #8b7455;
    --kraft-deep: #7a6448;
    --band-white: #ffffff;
    --ink-dark: #2e2519;
    --ink-olive: #6a5934;
    --icon-disc: #ddd1bb;
    --line-light: rgba(255,255,255,0.75);
    --text-light: #f6f0e4;
  }
  * { box-sizing: border-box; margin: 0; padding: 0; }
  html, body {
    width: 1200px; height: 1000px; overflow: hidden;
    background: var(--stage);
  }
  .sheet {
    width: 1200px; height: 1000px;
    display: flex; flex-direction: column; align-items: center; justify-content: center;
    gap: 52px;
  }
  .card {
    position: relative; width: 720px; height: 436px; overflow: hidden;
    box-shadow: 0 10px 30px rgba(0,0,0,0.35);
  }

  /* ---------- Front ---------- */
  .card-front {
    background: radial-gradient(ellipse at 70% 30%, var(--kraft-light), var(--kraft-mid) 85%);
  }
  .front-motif {
    position: absolute; left: 0; top: 0; width: 320px; height: 290px;
    background: radial-gradient(circle at 0% 90%, var(--kraft-mid) 0%, var(--kraft-pale) 55%, rgba(235,226,209,0) 100%);
  }
  .identity {
    position: absolute; left: 392px; top: 78px;
    font-family: "Cardo", Georgia, serif; color: var(--ink-dark);
  }
  .identity-name {
    font-size: 34px; font-weight: 700; letter-spacing: 2px; line-height: 1;
  }
  .identity-role {
    font-size: 22px; letter-spacing: 1.5px; margin-top: 6px; padding-left: 30px; color: #3c3226;
  }
  .contact-band {
    position: absolute; left: 0; right: 0; bottom: 0; height: 146px;
    background: var(--band-white);
    font-family: "Lato", Arial, sans-serif; color: var(--ink-olive);
  }
  .contact-item {
    position: absolute; display: flex; align-items: center; gap: 12px;
    font-size: 25px; letter-spacing: 0.5px; white-space: nowrap;
  }
  .contact-item svg { width: 34px; height: 34px; flex: none; }
  .contact-email { left: 30px; top: 62px; }
  .contact-phone { right: 44px; top: 18px; }
  .contact-web { right: 44px; top: 66px; font-size: 21px; }

  /* ---------- Back ---------- */
  .card-back {
    background: radial-gradient(ellipse at 40% 40%, var(--kraft-dark), var(--kraft-deep) 90%);
    color: var(--text-light); font-family: "Lato", Arial, sans-serif;
  }
  .fee { position: absolute; left: 36px; top: 28px; }
  .fee-label { font-size: 17px; letter-spacing: 1.5px; text-transform: uppercase; }
  .fee-amount { font-size: 52px; font-weight: 700; line-height: 1.05; }
  .class-list {
    position: absolute; left: 36px; top: 132px; width: 330px;
    display: flex; flex-direction: column; gap: 22px;
  }
  .class-row { display: flex; align-items: center; gap: 16px; }
  .class-tag {
    flex: none; width: 96px; padding: 7px 0; border-radius: 14px;
    background: var(--band-white); color: var(--ink-olive);
    font-size: 13px; font-weight: 700; letter-spacing: 1px; text-align: center;
  }
  .class-info { font-size: 15px; line-height: 1.45; }
  .divider-v {
    position: absolute; left: 392px; top: 36px; bottom: 36px; width: 1px;
    background: var(--line-light);
  }
  .trial { position: absolute; left: 420px; top: 44px; width: 270px; }
  .trial-title { font-size: 32px; line-height: 1.1; }
  .trial-note { font-size: 14px; margin-top: 8px; line-height: 1.4; }
  .divider-h {
    position: absolute; left: 420px; top: 182px; width: 264px; height: 1px;
    background: var(--line-light);
  }
  .message {
    position: absolute; left: 414px; top: 214px; width: 284px;
    font-family: "Cardo", Georgia, serif; font-size: 27px; letter-spacing: 3px;
    line-height: 1.45; text-align: center;
  }
</style>
</head>
<body>
<main class="sheet">

  <section class="card card-front" aria-label="Business card front">
    <div class="front-motif" role="img" aria-label="Decorative motif of soft concentric arcs in pale kraft tones"></div>

    <div class="identity">
      <h1 class="identity-name">MIKA ARAI</h1>
      <p class="identity-role">English Instructor</p>
    </div>

    <div class="contact-band">
      <div class="contact-item contact-email">
        <svg viewBox="0 0 34 34" aria-hidden="true">
          <circle cx="17" cy="17" r="17" fill="var(--icon-disc)"/>
          <rect x="9" y="11" width="16" height="12" fill="none" stroke="#fff" stroke-width="2"/>
          <path d="M9 11 L17 18 L25 11" fill="none" stroke="#fff" stroke-width="2"/>
        </svg>
        <span>mikaarai@mailbox.com</span>
      </div>
      <div class="contact-item contact-phone">
        <svg viewBox="0 0 34 34" aria-hidden="true">
          <circle cx="17" cy="17" r="17" fill="var(--icon-disc)"/>
          <rect x="11" y="8" width="12" height="18" rx="2" fill="none" stroke="#fff" stroke-width="2"/>
          <line x1="15" y1="22.5" x2="19" y2="22.5" stroke="#fff" stroke-width="2"/>
        </svg>
        <span>090-3217-6648</span>
      </div>
      <div class="contact-item contact-web">
        <span>www.mikaarai-english.com</span>
      </div>
    </div>
  </section>

  <section class="card card-back" aria-label="Business card back">
    <div class="fee">
      <p class="fee-label">Course fee:</p>
      <p class="fee-amount">3150 ¥ ~</p>
    </div>

    <div class="class-list">
      <div class="class-row">
        <span class="class-tag">KIDS</span>
        <p class="class-info">Mom &amp; Dad can join<br>30 minutes | 45 minutes</p>
      </div>
      <div class="class-row">
        <span class="class-tag">STUDENTS</span>
        <p class="class-info">Over age 13<br>60 minutes | 90 minutes</p>
      </div>
      <div class="class-row">
        <span class="class-tag">ADULTS</span>
        <p class="class-info">Over age 19<br>60 minutes | 90 minutes</p>
      </div>
    </div>

    <div class="divider-v"></div>

    <div class="trial">
      <p class="trial-title">free trial lesson</p>
      <p class="trial-note">Web Lesson &amp;<br>Face to Face Lesson available</p>
    </div>

    <div class="divider-h"></div>

    <p class="message">Feel free at asking me anything about my classes</p>
  </section>

</main>
</body>
</html>
```